Banner Ad Design Project

We need a server banner image for our web site. The banner is to sell dedicated servers. The size needs to be 732x138 pixels.

Here is an example of the background we're thinking about: http://www.quolventa.com/images/banners/qvbanner.png

But feel free to be creative, and design a banner that looks good on the following page: http://www.quolventa.com/marbexservers.asp

Incorporate some of these words in the banner as features:
-Rapid I/O SSD Hybrid RAID
-SLA Included
-Marbex Dorvo Processors
-24x7 Monitoring and Support

I like the colors on this banner... http://www.quolventa.com/images/banners/header-spring.png

so, maybe a white background would look good.

```html
<!DOCTYPE html>
<html lang="en">
<head>
<meta charset="utf-8">
<title>Rapid I/O SSD Hybrid RAID Banner</title>
<link href="https://fonts.googleapis.com/css2?family=PT+Sans+Narrow:wght@700&family=Questrial&display=swap" rel="stylesheet">
<style>
  :root {
    --frame: #b9b6b0;
    --rack-dark: #17130f;
    --rack-mid: #3a2d22;
    --rack-warm: #5a2a1c;
    --headline-top: #ffe14a;
    --headline-bottom: #e7a812;
    --headline-edge: #2a1a05;
    --tagline: #ffffff;
  }
  * { margin: 0; padding: 0; box-sizing: border-box; }
  html, body {
    width: 1200px;
    height: 226px;
    overflow: hidden;
    background: #ffffff;
  }
  .banner {
    position: relative;
    width: 1200px;
    height: 226px;
    border: 3px solid var(--frame);
    overflow: hidden;
  }
  .banner__backdrop {
    position: absolute;
    inset: 0;
    background:
      radial-gradient(ellipse 40% 60% at 18% 70%, rgba(120, 40, 25, 0.45), transparent 70%),
      radial-gradient(ellipse 35% 55% at 85% 75%, rgba(110, 35, 20, 0.4), transparent 70%),
      linear-gradient(180deg, var(--rack-mid) 0%, var(--rack-dark) 45%, var(--rack-mid) 75%, var(--rack-dark) 100%);
  }
  .banner__backdrop::after {
    content: "";
    position: absolute;
    inset: 0;
    background: rgba(10, 8, 6, 0.35);
  }
  .banner__content {
    position: relative;
    height: 100%;
    display: flex;
    flex-direction: column;
    align-items: center;
  }
  .banner__headline {
    margin-top: 28px;
    font-family: "PT Sans Narrow", "Arial Narrow", sans-serif;
    font-weight: 700;
    font-size: 88px;
    line-height: 1;
    letter-spacing: 0.5px;
    color: var(--headline-bottom);
    background: linear-gradient(180deg, var(--headline-top) 20%, var(--headline-bottom) 85%);
    -webkit-background-clip: text;
    background-clip: text;
    -webkit-text-fill-color: transparent;
    -webkit-text-stroke: 1.5px var(--headline-edge);
    filter: drop-shadow(0 3px 3px rgba(0, 0, 0, 0.85));
  }
  .banner__tagline {
    margin-top: 22px;
    font-family: "Questrial", "Century Gothic", sans-serif;
    font-size: 31px;
    line-height: 1;
    color: var(--tagline);
    text-shadow: 0 2px 3px rgba(0, 0, 0, 0.8);
  }
</style>
</head>
<body>
  <div class="banner">
    <div class="banner__backdrop" role="img" aria-label="Dimly lit rows of rack-mounted servers with red drive trays"></div>
    <div class="banner__content">
      <h1 class="banner__headline">Rapid I/O SSD Hybrid RAID</h1>
      <p class="banner__tagline">24x7 Monitoring and Support</p>
    </div>
  </div>
</body>
</html>
```